Fennel Cellar Online organic artisan and gourmet supermarket

Brief:
Brand: Fennel Cellar (FC) is an online store selling artisan and organinc Italian products. Our look and feel we have gone with is rustic, premium and unfiltered (visit us @ www.fennelcellar.com.au)
Our slogan: "cook Italy, eat Italy, love Italy"
Goals: prior to our online store going live, we used to attend a food market once a week. Due to unfortunate circumstances, we stopped. Since then, our store has gone live and wanted to use the card as a reminder we are back at the markets.
I also have a restaurant, "fennel ristorante" so I wanted to hand them out to customers in the restaurant but also act as reminder of our pop up market stores and our website to buy from.
Personality: FC is more than just a store. Our goal is to be not only a store but an informationa hub of Italian food.
We offer assistance to people who need help in their kitchen as well as catering
Logo: I have a logo which I was not able to upload.

Target Market(s)

Food lovers
Italian food interest
Wealthy
Organic gourmet food enthusiest

Industry/Entity Type

Store

Contact Information for Business Card

Shop online or visit us @ Willow Bend organic market
Ciao@fennelcellar.com.au
Www.fennelcellar.com.au

Online store, Cooking advice, catering, ristorante and information hub

Requirements
Must have
• Logo
• Information
• May be larger than a business card to fit information but smaller than a post card
• Need to look interesting and different
• Not a simple card design
Nice to have
• Different fonts
• Rustic looking
• Qwerky

```html
<!DOCTYPE html>
<html lang="en">
<head>
<meta charset="utf-8">
<title>Fennel Cellar – Business Card</title>
<link href="https://fonts.googleapis.com/css2?family=Open+Sans:wght@400;600&family=Pathway+Gothic+One&display=swap" rel="stylesheet">
<style>
  :root {
    --page-bg: #3a3a3a;
    --card-dark: #1b1b1b;
    --card-light: #f6f6f6;
    --card-light-shade: #e6e6e6;
    --photo-deep: #2a1d14;
    --photo-warm: #5b3b24;
    --ink-light: #ffffff;
    --ink-soft: #e8e8e8;
    --ink-dark: #1a1a1a;
    --rule: #8a8a8a;
  }
  * { margin: 0; padding: 0; box-sizing: border-box; }
  html, body { width: 1200px; height: 750px; overflow: hidden; }
  body {
    background: var(--page-bg);
    font-family: "Open Sans", Arial, sans-serif;
    position: relative;
  }
  .card {
    position: absolute;
    top: 228px;
    width: 461px;
    height: 262px;
    border-radius: 12px;
    overflow: hidden;
  }
  .card--front { left: 124px; background: var(--card-dark); }
  .card--back {
    left: 618px;
    background: radial-gradient(ellipse at center, var(--card-light) 55%, var(--card-light-shade) 100%);
    display: flex; align-items: center; justify-content: center;
  }

  .hero {
    position: absolute; left: 0; top: 0; width: 100%; height: 157px;
    background: linear-gradient(120deg, var(--photo-deep) 0%, var(--photo-warm) 50%, var(--photo-deep) 100%);
  }
  .hero-cross { position: absolute; left: 0; top: 0; width: 100%; height: 157px; }
  .hero-info {
    position: absolute; top: 54px;
    font-family: "Pathway Gothic One", "Arial Narrow", sans-serif;
    font-size: 15px; line-height: 17px;
    color: var(--ink-light);
    text-shadow: 0 1px 2px rgba(0,0,0,.8);
  }
  .hero-info--visit { left: 19px; }
  .hero-info--contact { right: 23px; text-align: right; }

  .tagline {
    position: absolute; left: 0; top: 171px; width: 100%;
    text-align: center; color: var(--ink-light);
  }
  .tagline-title { font-size: 14px; font-weight: 600; letter-spacing: .2px; }
  .tagline-services { font-size: 11px; line-height: 15px; color: var(--ink-soft); margin-top: 4px; }

  .social {
    position: absolute; left: 0; top: 230px; width: 100%;
    display: flex; align-items: center; justify-content: center; gap: 5px;
  }
  .social-rule { width: 62px; height: 1px; background: var(--rule); margin: 0 4px; }
  .social-dot {
    width: 19px; height: 19px; border-radius: 50%;
    border: 1px solid var(--ink-light);
  }

  .brand { display: flex; align-items: center; gap: 10px; }
  .brand-mark { width: 22px; height: 22px; border-radius: 50%; border: 2px solid var(--ink-dark); }
  .brand-name {
    font-family: "Open Sans", Arial, sans-serif;
    font-size: 22px; font-weight: 600; letter-spacing: 2px;
    color: var(--ink-dark); text-transform: uppercase;
  }
</style>
</head>
<body>
  <section class="card card--front">
    <div class="hero" role="img" aria-label="Rustic wooden board with Italian cheeses, cured ham and crusty bread"></div>
    <svg class="hero-cross" viewBox="0 0 461 157" aria-hidden="true">
      <line x1="152" y1="0" x2="310" y2="157" stroke="#fff" stroke-width="2"/>
      <line x1="311" y1="0" x2="153" y2="157" stroke="#fff" stroke-width="2"/>
    </svg>
    <div class="hero-info hero-info--visit">
      Shop online or visit us<br>
      @ Willow Bend organic market<br>
      48 Linden St, Millbrook, 2093
    </div>
    <div class="hero-info hero-info--contact">
      Phone : (02) 5550 1827<br>
      Ciao@fennelcellar.com.au<br>
      www.fennelcellar.com.au
    </div>
    <div class="tagline">
      <p class="tagline-title">COOK ITALY, EAT ITALY, LOVE ITALY</p>
      <p class="tagline-services">Online store • Cooking advice<br>Catering • Ristorante and information hub</p>
    </div>
    <div class="social">
      <span class="social-rule"></span>
      <span class="social-dot"></span>
      <span class="social-dot"></span>
      <span class="social-dot"></span>
      <span class="social-rule"></span>
    </div>
  </section>

  <section class="card card--back">
    <div class="brand">
      <span class="brand-mark"></span>
      <span class="brand-name">Fennel Cellar</span>
    </div>
  </section>
</body>
</html>
```